Mirela Causo Photography

I need a website design for my photography business, I want something clean, elegant, Classy.. I like the colors, White, Black, Green/Blue, Pink, Brown, Lavender,, I have a lot added my Logo .... Additional Info... I need a Photography Website Design, with probably 6 Tabs, Home, About Me, Portfolio, Gallery, Investment, Contact.
Home Page should have my logo, Name & Address, Social Media Icons, and Pictures.
As long as the templates are made I have a hosting coming that will code it.
Target Market(s)
Portraits Photography, Senior Portraits, Newborn, Families, Events, Engagements, Wedding,
Industry/Entity Type
Business
Number of Pages Required
5+ page
Look and feel

```html
<!DOCTYPE html>
<html lang="en">
<head>
<meta charset="utf-8">
<title>Mirela Causo Photography</title>
<link rel="stylesheet" href="https://fonts.googleapis.com/css2?family=Great+Vibes&family=Questrial&display=swap">
<style>
:root{
  --pink:#e895c6;
  --pink-soft:#ecaed3;
  --pink-overlay:rgba(226,140,190,.78);
  --ink:#111;
  --grey:#8a8a8a;
  --line:#d9d9d9;
  --white:#fff;
  --black:#000;
}
*{margin:0;padding:0;box-sizing:border-box}
html,body{width:1200px;height:2933px;overflow:hidden;background:var(--white)}
body{position:relative;font-family:"Questrial",sans-serif;color:var(--grey)}
.abs{position:absolute}

/* hero */
.hero{left:0;top:0;width:1200px;height:809px;
  background:radial-gradient(ellipse at 50% 45%,#6e6e6e 0%,#4a4a4a 40%,#2c2c2c 100%)}
.brand{left:195px;top:18px;width:230px;color:var(--white);text-align:center}
.brand-dot{display:block;margin:0 auto 6px;width:48px;height:48px;border-radius:50%;background:var(--white)}
.brand-name{font-size:46px;line-height:44px;letter-spacing:1px}
.brand-sub{font-size:13px;letter-spacing:6px;margin-top:2px}
.socials-top{right:180px;top:14px;display:flex;gap:20px}
.socials-top span{width:14px;height:14px;border-radius:50%;background:var(--pink-soft)}
.phone-top{left:892px;top:56px;color:var(--white);font-size:17px;display:flex;align-items:center;gap:10px}
.nav{left:510px;top:106px;display:flex;gap:0;font-size:13px;color:var(--white);letter-spacing:.5px}
.nav a{color:inherit;text-decoration:none;margin-right:32px}
.nav a.active{color:var(--pink)}
.hero-name{left:0;width:1200px;top:335px;text-align:center;font-family:"Great Vibes",cursive;font-size:130px;color:#fbe6f2;line-height:130px}
.hero-role{left:0;width:1200px;top:462px;text-align:center;color:var(--white);font-size:23px;letter-spacing:1px}
.hero-btn{left:398px;top:584px;width:387px;height:69px;border:1px solid var(--white);color:var(--pink);font-size:30px;display:flex;align-items:center;justify-content:center}

/* sections */
.section-title{left:0;width:1200px;text-align:center;color:var(--pink);font-size:29px;letter-spacing:1px}
.about-text{left:200px;top:918px;width:800px;text-align:center;font-size:18px;line-height:22px;color:#9a9a9a}
.about-text b{color:var(--ink);font-weight:normal}
.about-rule{left:506px;top:1002px;width:174px;height:1px;background:var(--grey)}

.portfolio{left:0;top:1139px;width:1200px;height:379px;display:flex}
.panel{flex:0 0 auto;height:379px;position:relative}
.panel-a{width:403px;background:linear-gradient(135deg,#d98bb8,#c97aa9 60%,#e3a0c8)}
.panel-b{width:394px;background:linear-gradient(180deg,#cfc6bd 0%,#8c7f77 35%,#3c3434 75%,#2a2424 100%)}
.panel-c{width:403px;background:linear-gradient(180deg,#e6a3cb,#dc93c0 60%,#e9b2d4)}
.panel-copy{position:absolute;left:28px;right:28px;top:194px;text-align:center;color:var(--white);font-size:14px;line-height:17px}
.panel-more{position:absolute;left:0;right:0;bottom:10px;text-align:center;color:#ccc;font-size:13px}

.tile{border:4px solid var(--pink-soft)}
.t1{left:171px;top:1660px;width:301px;height:183px;background:linear-gradient(180deg,#6f7a84,#4a4a4a)}
.t2{left:171px;top:1858px;width:301px;height:185px;background:linear-gradient(180deg,#2e3a44,#3d4a55 60%,#5b6470)}
.t3{left:481px;top:1660px;width:291px;height:232px;background:linear-gradient(180deg,#9fb2c4,#7a5a52 60%,#6a6a6a)}
.t4{left:481px;top:1901px;width:291px;height:233px;background:linear-gradient(180deg,#b9c3c9,#e3d9cb 45%,#d9a491 75%,#efe6dc)}
.t5{left:782px;top:1660px;width:242px;height:393px;background:linear-gradient(180deg,#1e1e1e,#4e4e4e 50%,#1a1a1a)}
.view-btn{left:870px;top:2099px;width:159px;height:37px;border:1px solid var(--pink-soft);color:var(--pink);font-size:15px;display:flex;align-items:center;justify-content:center}

.field{border:1px solid var(--line);color:#aaa;font-size:13px;letter-spacing:1px;padding:11px 10px}
.send{left:296px;top:2574px;width:633px;height:34px;background:var(--pink-soft);color:var(--white);font-size:13px;letter-spacing:2px;display:flex;align-items:center;justify-content:center}

/* footer */
.footer{left:0;top:2679px;width:1200px;height:254px;background:var(--black)}
.foot-line{left:0;width:1200px;display:flex;justify-content:center;align-items:center;gap:10px;color:var(--white)}
.foot-icon{width:20px;height:20px;border-radius:50%;background:var(--pink-soft);display:flex;align-items:center;justify-content:center}
.socials-foot{left:450px;top:2822px;width:300px;display:flex;justify-content:space-between}
.socials-foot span{width:36px;height:36px;border-radius:50%;background:var(--pink-soft)}
.copyright{left:0;width:1200px;top:2888px;text-align:center;color:var(--white);font-size:13px}
.foot-brand{left:848px;top:2830px;width:140px;text-align:center;color:#3a3a3a}
</style>
</head>
<body>

<div class="abs hero" role="img" aria-label="Black and white photo of a woman holding a camera at her waist"></div>

<div class="abs brand">
  <span class="brand-dot"></span>
  <div class="brand-name">mirela causo</div>
  <div class="brand-sub">PHOTOGRAPHY</div>
</div>

<div class="abs socials-top"><span></span><span></span><span></span><span></span><span></span></div>
<div class="abs phone-top">
  <svg width="12" height="20" viewBox="0 0 12 20"><rect x="1" y="1" width="10" height="18" rx="2" fill="none" stroke="#ecaed3" stroke-width="2"/><circle cx="6" cy="15.5" r="1.2" fill="#ecaed3"/></svg>
  0100-555-782
</div>

<nav class="abs nav">
  <a class="active" href="#">HOME</a><a href="#">ABOUT ME</a><a href="#">PORTFOLIO</a><a href="#">GALLERY</a><a href="#">INVESTMENT</a><a href="#">CONTACT</a>
</nav>

<div class="abs hero-name">mirela causo</div>
<div class="abs hero-role">PROFESSIONAL PHOTOGRAPHER</div>
<div class="abs hero-btn">PORTFOLIO</div>

<h2 class="abs section-title" style="top:850px;font-weight:normal">ABOUT ME</h2>
<p class="abs about-text">Lorem ipsum dolor sit amet, <b>consectetuer adipiscing</b> elit, sed diam nonummy nibh euismod tincidunt ut laoreet dolore magna aliquam erat volutpat. Ut wisi enim ad minim veniam, <b>quis nostrud exerci</b> tation ullamcorper suscipit lobortis nisl ut aliquip ex ea commodo consequat.</p>
<div class="abs about-rule"></div>

<h2 class="abs section-title" style="top:1068px;font-weight:normal">PORTFOLIO</h2>
<div class="abs portfolio">
  <div class="panel panel-a" role="img" aria-label="Pink toned photo of hands holding a camera"></div>
  <div class="panel panel-b" role="img" aria-label="Photo of a person looking over a city skyline at dusk">
    <p class="panel-copy">Lorem ipsum dolor sit amet, consectetuer adipiscing elit, sed diam nonummy nibh euismod tincidunt ut laoreet dolore magna aliquam erat volutpat.</p>
    <span class="panel-more">Read more</span>
  </div>
  <div class="panel panel-c" role="img" aria-label="Pink toned photo of a person standing by the sea"></div>
</div>

<h2 class="abs section-title" style="top:1578px;font-weight:normal">GALLERY</h2>
<div class="abs tile t1" role="img" aria-label="Photo of a busy city street with traffic"></div>
<div class="abs tile t2" role="img" aria-label="Photo of a hooded figure among white flowers"></div>
<div class="abs tile t3" role="img" aria-label="Photo of a suspension bridge walkway"></div>
<div class="abs tile t4" role="img" aria-label="Photo of people lying on a beach"></div>
<div class="abs tile t5" role="img" aria-label="Black and white photo of musicians on stage"></div>
<div class="abs view-btn">VIEW GALLERY</div>

<h2 class="abs section-title" style="top:2240px;font-weight:normal">CONTACT &nbsp;US</h2>
<div class="abs field" style="left:296px;top:2310px;width:312px;height:39px">NAME</div>
<div class="abs field" style="left:616px;top:2310px;width:313px;height:39px">LAST NAME</div>
<div class="abs field" style="left:296px;top:2354px;width:312px;height:39px">EMAIL</div>
<div class="abs field" style="left:616px;top:2354px;width:313px;height:39px">PHONE</div>
<div class="abs field" style="left:296px;top:2400px;width:633px;height:169px">MESSAGE</div>
<div class="abs send">SEND</div>

<footer class="abs footer"></footer>
<div class="abs foot-line" style="top:2732px;font-size:15px">
  <span class="foot-icon"><svg width="10" height="13" viewBox="0 0 10 13"><path d="M5 0a5 5 0 0 0-5 5c0 3.5 5 8 5 8s5-4.5 5-8a5 5 0 0 0-5-5z" fill="#000"/><circle cx="5" cy="5" r="1.8" fill="#ecaed3"/></svg></span>
  418 Linden Park Road &nbsp;Harwick, NY 10592
</div>
<div class="abs foot-line" style="top:2773px;font-size:19px">
  <span class="foot-icon"><svg width="10" height="12" viewBox="0 0 10 12"><rect x="2" y="0.5" width="6" height="11" rx="1" fill="#000"/></svg></span>
  0100-555-782
</div>
<div class="abs socials-foot"><span></span><span></span><span></span><span></span><span></span></div>
<div class="abs copyright">©2015 copyright.mirelacausophotography.com</div>
<div class="abs foot-brand">
  <div style="width:34px;height:34px;border-radius:50%;background:#3a3a3a;margin:0 auto 4px"></div>
  <div style="font-size:26px;line-height:26px">mirela causo</div>
  <div style="font-size:8px;letter-spacing:4px">PHOTOGRAPHY</div>
</div>

</body>
</html>
```